KRV Business Cards

We are a local commercial development company based in Silicon Valley and we would like a new business card. I've attached a copy of our company brochure to give a flavor of what we do, our logo, info company colors/graphics, and our current business card. We don't necessarily need a crazy makeover, but would like something that feels a little bit more "fresh" and modern (we've had the same business card design for 15+ years), but still in keeping with our overall brand -- clean, high-quality, modern but timeless. Would like to add our website to the info on the card (www.velmara.com) and would like the flexibility for some folks to have an efax number listed and some not to have that included (without it looking like there is a hole).

```html
<!DOCTYPE html>
<html lang="en">
<head>
<meta charset="utf-8">
<title>KRV Business Cards</title>
<link href="https://fonts.googleapis.com/css2?family=Nunito+Sans:ital,wght@0,400;1,400&display=swap" rel="stylesheet">
<style>
  :root {
    --stage: #181818;
    --navy-dark: #2b465f;
    --navy: #2e4d6a;
    --navy-panel: #37556f;
    --navy-shade: #2f4962;
    --frame-gold: #8c8b85;
    --ivory: #eef2f5;
    --paper: #ffffff;
    --paper-shade: #f3f3f3;
    --ink: #1c1c1c;
    --ink-soft: #333333;
  }
  html, body {
    margin: 0;
    width: 1200px;
    height: 1200px;
    overflow: hidden;
    background: var(--stage);
  }
  .card {
    position: absolute;
    left: 165px;
    width: 870px;
    display: block;
  }
  .card--front { top: 106px; height: 458px; }
  .card--back { top: 638px; height: 457px; }
  .company-name {
    font-family: "Nunito Sans", sans-serif;
    font-weight: 400;
    fill: var(--ivory);
    letter-spacing: 1px;
  }
  .company-name--large { font-size: 30px; }
  .company-name--small { font-size: 21px; letter-spacing: 0.5px; }
  .website {
    font-family: "Nunito Sans", sans-serif;
    font-size: 17px;
    fill: #dde5ec;
    letter-spacing: 0.5px;
  }
  .person-name {
    font-family: "Nunito Sans", sans-serif;
    font-size: 26px;
    fill: var(--ink);
  }
  .person-title {
    font-family: "Nunito Sans", sans-serif;
    font-style: italic;
    font-size: 13.5px;
    fill: var(--ink-soft);
    letter-spacing: 0.6px;
  }
  .contact-line {
    font-family: "Nunito Sans", sans-serif;
    font-size: 14px;
    fill: var(--ink-soft);
  }
  .contact-icon { fill: var(--ink); }
</style>
</head>
<body>

<svg class="card card--front" viewBox="0 0 870 458" aria-label="Business card front">
  <rect class="band band--top" x="0" y="0" width="870" height="232" fill="var(--navy-dark)"/>
  <rect class="band band--bottom" x="0" y="232" width="870" height="226" fill="var(--navy)"/>
  <rect class="edge-frame" x="13" y="13" width="844" height="432" fill="none" stroke="var(--frame-gold)" stroke-width="3"/>
  <rect class="name-mark" x="215" y="220" width="22" height="22" fill="var(--ivory)"/>
  <text class="company-name company-name--large" x="252" y="242">KRV Development Company, LLC</text>
</svg>

<svg class="card card--back" viewBox="0 0 870 457" aria-label="Business card back">
  <defs>
    <linearGradient id="fold-shade" x1="0" y1="0" x2="1" y2="0">
      <stop offset="0" stop-color="#bdbdbd"/>
      <stop offset="1" stop-color="#ffffff" stop-opacity="0"/>
    </linearGradient>
  </defs>
  <rect class="card-paper" x="0" y="0" width="870" height="457" fill="var(--paper)"/>

  <rect class="brand-panel" x="11" y="11" width="402" height="435" fill="var(--navy-panel)"/>
  <polygon class="brand-panel-shade" points="413,11 413,446 40,446" fill="var(--navy-shade)"/>

  <rect class="info-panel" x="413" y="11" width="446" height="435" fill="var(--paper)" stroke="#5a5a5a" stroke-width="1"/>
  <polygon class="info-panel-shade" points="413,11 858.5,445.5 413,445.5" fill="var(--paper-shade)"/>
  <rect class="info-panel-fold" x="413.5" y="11.5" width="30" height="434" fill="url(#fold-shade)"/>

  <text class="company-name company-name--small" x="212" y="236" text-anchor="middle">KRV Development Company, LLC</text>
  <text class="website" x="212" y="364" text-anchor="middle">www.velmara.com</text>

  <text class="person-name" x="779" y="157" text-anchor="end">DANA L WHITFORD</text>
  <text class="person-title" x="779" y="175" text-anchor="end">PARTNER</text>

  <g class="contact-icon icon-phone" transform="translate(536,228)">
    <path d="M3 0 L6 0 L7.5 4 L5.5 6 C6.5 8.5 8.5 10.5 11 11.5 L13 9.5 L17 11 L17 14 C17 15.5 16 16 15 16 C7 15.5 1.5 10 1 2 C1 1 1.5 0 3 0 Z"/>
  </g>
  <text class="contact-line" x="565" y="241">555 214 0386, 5552140387</text>

  <g class="contact-icon icon-fax" transform="translate(536,262)">
    <rect x="4" y="0" width="10" height="6" fill="none" stroke="var(--ink)" stroke-width="1.6"/>
    <rect x="0" y="6" width="18" height="10" rx="1.5"/>
    <rect x="4" y="10" width="10" height="1.4" fill="#ffffff"/>
    <rect x="4" y="12.8" width="10" height="1.4" fill="#ffffff"/>
  </g>
  <text class="contact-line" x="565" y="274">5552149012</text>

  <g class="contact-icon icon-mail" transform="translate(536,292)">
    <rect x="0" y="0" width="18" height="12"/>
    <polyline points="0.8,0.8 9,7 17.2,0.8" fill="none" stroke="#ffffff" stroke-width="1.3"/>
  </g>
  <text class="contact-line" x="565" y="303">dana@velmara.com</text>

  <g class="contact-icon icon-pin" transform="translate(537,320)">
    <path d="M8 0 C3.6 0 0 3.4 0 7.6 C0 12.8 8 20 8 20 C8 20 16 12.8 16 7.6 C16 3.4 12.4 0 8 0 Z M8 4.6 A3 3 0 1 1 8 10.6 A3 3 0 1 1 8 4.6 Z" fill-rule="evenodd"/>
  </g>
  <text class="contact-line" x="565" y="334">218 Linden Street, Menlo Park,</text>
  <text class="contact-line" x="565" y="351">California 94025</text>
</svg>

</body>
</html>
```